依頼詳細
ターゲットは、墓地を探している方です。生前墓、小規模墓地、ペットと共に墓地に入れる敷地も用意されています。
サイトURL
http://www.hotarudaireien.jp/
ページ数
1ページ
希望イメージ
シンプル 複雑
単色 カラフル
暗い 明るい
日常 高級
遊び心 厳粛
未来的 伝統的
女性的 男性的
希望する色
緑 青
納品ファイル
• イラストレーター形式 (.ai)
補足説明
サイトレイアウトのPDFデータです。

弊社お客様にデザインを選んでいただきました。
お客様のイメージと一致したようでとても喜んでいただきました。

すばらしいデザインをありがとうございました。
24デザインの中からお客様に選んでいただきました。
お客様はとても喜んでおります。
今後ともよろしくお願いします。

```html
<!DOCTYPE html>
<html lang="ja">
<head>
<meta charset="utf-8">
<title>蛍台霊園</title>
<link href="https://fonts.googleapis.com/css2?family=Noto+Sans+JP:wght@400;700&family=Noto+Serif+JP:wght@500;700&display=swap" rel="stylesheet">
<style>
:root{
  --green:#5e7f2c;
  --green-dark:#3f5a1c;
  --green-light:#8aa84a;
  --green-pale:#e6eed6;
  --cream:#f7f5ee;
  --line:#cfd8b8;
  --text:#333;
  --purple:#6a4a78;
  --white:#fff;
}
*{margin:0;padding:0;box-sizing:border-box}
html,body{width:1200px;height:2581px;overflow:hidden}
body{font-family:"Noto Sans JP",sans-serif;color:var(--text);background:var(--cream);font-size:22px}
.header{height:120px;background:var(--white);display:flex;align-items:center;padding:0 36px;justify-content:space-between}
.brand{display:flex;align-items:center;gap:22px}
.brand-mark{width:84px;height:84px;background:var(--green)}
.brand-name{font-family:"Noto Serif JP",serif;font-weight:700;font-size:52px;color:var(--green-dark);letter-spacing:6px}
.tel-box{display:flex;align-items:center;gap:14px;background:var(--green);color:var(--white);padding:12px 22px;border-radius:6px}
.tel-box small{font-size:20px}
.tel-box strong{font-size:36px;letter-spacing:1px}
.nav{height:48px;background:var(--green);display:flex}
.nav a{flex:1;color:var(--white);text-decoration:none;font-size:19px;display:flex;align-items:center;justify-content:center;border-right:1px solid var(--green-light)}
.nav a:first-child{background:var(--green-dark)}
.hero{position:relative;height:652px;background:linear-gradient(180deg,#cfe0ee 0%,#e4ecf2 38%,#8fa86a 60%,#a9a89c 80%,#c8c5bb 100%)}
.hero-copy{position:absolute;right:180px;top:40px;writing-mode:vertical-rl;font-family:"Noto Serif JP",serif;color:var(--white);text-shadow:0 0 6px rgba(0,0,0,.35);display:flex;gap:26px}
.hero-copy .big{font-size:56px;letter-spacing:10px}
.hero-copy .small{font-size:30px;letter-spacing:8px;margin-top:60px}
.main{display:flex;gap:40px;padding:28px 32px 0;height:1440px}
.side{width:288px;flex:none}
.side-box{border:2px solid var(--green-light);background:var(--white);margin-bottom:16px}
.side-box h3{background:var(--green);color:var(--white);font-family:"Noto Serif JP",serif;font-size:30px;padding:12px 16px;border-bottom:4px solid var(--green-light)}
.side-box li{list-style:none;font-size:21px;padding:11px 18px;border-bottom:1px dotted var(--line);color:var(--green-dark)}
.side-box li::before{content:"▶";font-size:13px;color:var(--green-light);margin-right:10px;vertical-align:middle}
.access-photo{height:150px;margin:14px;background:linear-gradient(180deg,#b9c9a6,#7f9560)}
.access-text{font-size:17px;line-height:1.7;padding:0 14px 14px}
.access-text b{display:block;font-size:22px;color:var(--green-dark);margin-top:8px}
.map-btn{display:block;background:var(--green-light);color:var(--white);text-align:center;font-size:24px;font-weight:700;padding:16px;border-radius:8px;border:3px solid var(--green);text-decoration:none}
.content{flex:1}
.section{background:var(--white);margin-bottom:28px;padding:0 0 24px}
.section h2{font-family:"Noto Serif JP",serif;font-size:34px;color:var(--green-dark);padding:18px 24px;border-bottom:3px solid var(--green-pale);border-left:10px solid var(--green)}
.section p{font-size:19px;line-height:1.9;padding:14px 24px 0}
.topics h2{color:var(--purple);border-left-color:var(--purple)}
.topics li{list-style:none;display:flex;gap:36px;font-size:19px;padding:16px 24px;border-bottom:1px dotted var(--line)}
.topics time{color:var(--green);flex:none}
.footer{position:absolute;top:2240px;left:0;width:1200px;height:341px;background:var(--green-dark);color:var(--white)}
.footer-inner{display:flex;align-items:center;justify-content:space-between;padding:56px 48px 0}
.footer .brand-name{color:var(--white);font-size:44px}
.footer .brand-sub{font-size:18px;margin-top:8px}
.footer .tel-box{background:var(--green);border:2px solid var(--green-light);flex-direction:column;gap:2px}
.footer-links{display:grid;grid-template-columns:repeat(2,160px);gap:8px 16px;font-size:18px}
.copyright{position:absolute;bottom:0;width:100%;height:56px;background:var(--green-pale);color:var(--green-dark);font-size:16px;display:flex;align-items:center;justify-content:center}
</style>
</head>
<body>
<header class="header">
  <div class="brand"><span class="brand-mark"></span><span class="brand-name">蛍台霊園</span></div>
  <div class="tel-box"><small>お問合せ</small>
    <svg width="34" height="34" viewBox="0 0 24 24"><path fill="#fff" d="M6.6 10.8a15 15 0 006.6 6.6l2.2-2.2a1 1 0 011-.25 11.4 11.4 0 003.6.57 1 1 0 011 1V20a1 1 0 01-1 1A17 17 0 013 4a1 1 0 011-1h3.5a1 1 0 011 1 11.4 11.4 0 00.57 3.6 1 1 0 01-.25 1z"/></svg>
    <strong>0120-48-213</strong></div>
</header>
<nav class="nav">
  <a>HOME</a><a>墓地施設紹介</a><a>地図・アクセス</a><a>墓地申込</a><a>お客様の声</a><a>墓地紹介</a><a>お問い合わせ</a>
</nav>
<div class="hero" role="img" aria-label="青空の下に広がる霊園の墓石と芝生の風景写真">
  <div class="hero-copy">
    <span class="small">やすらぎの丘　蛍台霊園</span>
    <span class="big">すべての御霊の</span>
    <span class="big">安らかなることを</span>
  </div>
</div>
<div class="main">
  <aside class="side">
    <div class="side-box"><h3>お客様の声</h3><ul>
      <li>宇都宮市 鈴木様</li><li>東京都 山本様</li><li>日光市 佐藤様</li><li>千葉県 後藤様</li><li>埼玉県 越後様</li></ul></div>
    <div class="side-box"><h3>周辺施設のご案内</h3><ul>
      <li>ダミーテキスト</li><li>ダミーテキスト</li><li>ダミーテキスト</li><li>ダミーテキスト</li><li>ダミーテキスト</li></ul></div>
    <div class="side-box"><h3>アクセス</h3>
      <div class="access-photo" role="img" aria-label="霊園管理事務所の建物外観写真"></div>
      <div class="access-text">東北自動車道インターより約10分。日光街道沿いの静かな丘の上にあり、市街地からもお車で気軽にお越しいただけます。
        <b>蛍台霊園 管理事務所</b>栃木県日光市蛍台1204-5<br>TEL 0288-40-1192<br>FAX 0288-40-1193</div>
    </div>
    <a class="map-btn">詳しい地図はこちら</a>
  </aside>
  <div class="content">
    <section class="section">
      <h2>蛍台霊園について</h2>
      <p>緑と青空に包まれた永遠の安らぎの地。豊かな自然に囲まれた閑静な環境です。</p>
      <p>市街地からも近く、高速道路のインターからも車で約10分と、お参りにも便利な立地です。</p>
      <p>法事会館と休憩所を併設しており、少人数から大人数までご利用いただけます。お食事も手配いたします。</p>
      <p>宗旨・宗派は問いません。どなたでもご利用いただけます。(墓石は当苑指定となります)</p>
      <p>生前墓・小規模墓地のほか、ペットと一緒に眠れる区画もご用意しています。</p>
      <p>ご見学・お申込みは随時受け付けております。お気軽にお問い合わせください。</p>
      <p>墓地・墓石のお求めにはローン分割のご利用も可能です。</p>
    </section>
    <section class="section">
      <h2>霊園について</h2>
      <p>霊園と墓地のご案内。ダミーテキストダミーテキストダミーテキストダミーテキストダミーテキストダミーテキストダミーテキストダミーテキストダミーテキストダミーテキストダミーテキストダミーテキストダミーテキストダミーテキストダミーテキストダミーテキストダミーテキストダミーテキストダミーテキストダミーテキストダミーテキストダミーテキストダミーテキストダミーテキストダミーテキストダミーテキストダミーテキストダミーテキスト</p>
    </section>
    <section class="section topics">
      <h2>トピックス</h2>
      <ul>
        <li><time>2014年5月28日</time>ダミーテキストダミーテキストダミーテキスト</li>
        <li><time>2014年4月28日</time>ダミーテキストダミーテキストダミーテキスト</li>
        <li><time>2014年3月28日</time>ダミーテキストダミーテキストダミーテキスト</li>
        <li><time>2014年2月28日</time>ダミーテキストダミーテキストダミーテキスト</li>
        <li><time>2014年1月28日</time>ダミーテキストダミーテキストダミーテキスト</li>
      </ul>
    </section>
  </div>
</div>
<footer class="footer">
  <div class="footer-inner">
    <div><div class="brand-name">蛍台霊園</div><div class="brand-sub">栃木県日光市蛍台1204-5</div></div>
    <div class="tel-box"><small>お問い合わせはこちら</small><strong>0120-48-213</strong></div>
    <div class="footer-links"><span>HOME</span><span>お客様の声</span><span>墓地施設紹介</span><span>墓地紹介</span><span>地図・アクセス</span><span>お問い合わせ</span><span>墓地申込</span></div>
  </div>
  <div class="copyright">Copyright(C)hotarudaireien.jp All Rights Reserved.</div>
</footer>
</body>
</html>
```